RM BIZ CARDS

Hi,

Is it possible to see a one sided version (with logo and info) as well as a two-sided version (front side w/logo and back side with info)?
How do we choose card stock and finish once we approve a design?

We would like the following info included:

Peter Lowell
Rosfeld Talent Media
4127 Marwick Lane, Suite 300
Los Angeles, CA 90041
(323) 555-0148
peter@rosfeldtalentmedia.example

```html
<!DOCTYPE html>
<html lang="en">
<head>
<meta charset="utf-8">
<title>RM Business Cards</title>
<link href="https://fonts.googleapis.com/css2?family=Montserrat:wght@300;400;600&display=swap" rel="stylesheet">
<style>
  :root {
    --backdrop-light: #5a5a5a;
    --backdrop-dark: #1c1c1c;
    --card-black: #050505;
    --card-white: #ffffff;
    --ink-light: #f2f2f2;
    --ink-dark: #111111;
    --rule: #1a1a1a;
  }
  * { margin: 0; padding: 0; box-sizing: border-box; }
  html, body { width: 1200px; height: 880px; overflow: hidden; }
  body {
    position: relative;
    background: radial-gradient(ellipse at 55% 25%, var(--backdrop-light), var(--backdrop-dark) 75%);
    font-family: "Montserrat", sans-serif;
  }
  .card {
    position: absolute;
    width: 560px;
    height: 320px;
    border-radius: 22px;
    box-shadow: 0 18px 40px rgba(0,0,0,0.55);
  }
  .card-front {
    left: 90px;
    top: 90px;
    background: var(--card-black);
    color: var(--ink-light);
    display: flex;
    align-items: center;
    justify-content: center;
  }
  .brand {
    display: flex;
    align-items: center;
    gap: 16px;
  }
  .brand-dot {
    width: 34px;
    height: 34px;
    border: 2px solid var(--ink-light);
    border-radius: 50%;
  }
  .brand-name {
    font-weight: 300;
    font-size: 26px;
    letter-spacing: 5px;
    text-transform: uppercase;
  }
  .card-back {
    left: 550px;
    top: 470px;
    background: var(--card-white);
    color: var(--ink-dark);
  }
  .divider {
    position: absolute;
    left: 262px;
    top: 36px;
    width: 2px;
    height: 250px;
    background: var(--rule);
  }
  .identity {
    position: absolute;
    right: 318px;
    top: 44px;
    text-align: right;
  }
  .person-name { font-weight: 600; font-size: 16px; }
  .company-name { font-weight: 400; font-size: 13px; }
  .contact {
    position: absolute;
    left: 282px;
    bottom: 40px;
    font-size: 13px;
    line-height: 1.45;
  }
  .address { margin-bottom: 12px; }
  .contact-line { display: flex; align-items: center; gap: 7px; }
  .contact-line svg { width: 15px; height: 15px; flex: none; }
</style>
</head>
<body>
  <section class="card card-front">
    <div class="brand">
      <span class="brand-dot"></span>
      <span class="brand-name">Rosfeld Artist</span>
    </div>
  </section>

  <section class="card card-back">
    <div class="identity">
      <p class="person-name">Peter Lowell</p>
      <p class="company-name">Rosfeld Talent Media</p>
    </div>
    <div class="divider"></div>
    <div class="contact">
      <p class="address">4127 Marwick Lane, Suite 300<br>Los Angeles, CA 90041</p>
      <p class="contact-line">
        <svg viewBox="0 0 16 16" aria-hidden="true"><circle cx="8" cy="8" r="8" fill="#111"/><path d="M5 4.5c.6-.4 1.2-.2 1.5.3l.6 1.2c.2.4 0 .8-.3 1l-.5.3c.4.9 1.2 1.7 2.1 2.1l.3-.5c.2-.3.6-.5 1-.3l1.2.6c.5.3.7.9.3 1.5-.6.8-1.6 1-2.5.6C7 10.5 5.5 9 4.7 7.3c-.4-.9-.3-2 .3-2.8z" fill="#fff"/></svg>
        (323) 555-0148
      </p>
      <p class="contact-line">
        <svg viewBox="0 0 16 16" aria-hidden="true"><circle cx="8" cy="8" r="8" fill="#111"/><rect x="4" y="5.2" width="8" height="5.6" rx=".6" fill="#fff"/><path d="M4.3 5.6 8 8.4l3.7-2.8" fill="none" stroke="#111" stroke-width=".8"/></svg>
        peter@rosfeldtalentmedia.example
      </p>
    </div>
  </section>
</body>
</html>
```